Tarjetas de visita para empresa de aluminio

Empresa con mas de 40 años vendiendo perfiles de aluminio.
Somos fábrica y almacén, queremos renovar la tarjeta de presentación de nuestros comerciales dando una imgen innovadora y tecnógica mezclado con la calidez del respeto al medio ambiente.
Añado el logo de la empresa y actual cara trasera de la tarjeta de visita, el logo es el simbolo WM y la marca TRAVENIC EXTRUSION, la frase 2extrusion y lacado de aluminio" debe cambiarse por "Diseño, extrusión, lacado, anodizado y mecanizado de precisión de aluminio" o en su defecto incluir todos esos servicios que hacemos o una frase mas pegadiza.

We are an aluminium factory, we produce and stock profiles of aluminium.
we want to renew visit card of our sellers, we are looking for something that show innovation, tecnology and environment respect.
Upload our actual logo and back of visit card, logo WM and brand TRAVENIC EXTRUSION must be keept.
Text "Extrusion y lacado de aluminio" must be changed for "Diseño, extrusion, lacado, anodizado y mecanizado de precisión de aluminio" or something like that

```html
<!DOCTYPE html>
<html lang="es">
<head>
<meta charset="utf-8">
<title>Travenic Extrusion – Tarjeta de visita</title>
<link href="https://fonts.googleapis.com/css2?family=Fira+Sans+Condensed:wght@400;600&family=Lato:wght@400&family=Plus+Jakarta+Sans:wght@500;700&display=swap" rel="stylesheet">
<style>
  :root{
    --brand-blue:#2e5e87;
    --brand-blue-deep:#2a5a82;
    --steel:#93adbd;
    --ink:#3d3d3d;
    --silver:#d5dbe0;
    --white:#ffffff;
    --frame:#8a8a8a;
  }
  *{margin:0;padding:0;box-sizing:border-box}
  html,body{width:1200px;height:1200px;overflow:hidden;background:var(--white)}
  .canvas{position:relative;width:1200px;height:1200px}
  .card{position:absolute;left:185px;width:821px;height:462px}
  .card--front{top:118px;background:var(--brand-blue)}
  .card--back{top:610px;background:var(--white);border:1px solid var(--frame)}
  .brand-block{position:absolute;background:var(--brand-blue-deep);display:flex;flex-direction:column;align-items:center;justify-content:center}
  .brand-mark{border:3px solid var(--silver);border-radius:50%}
  .brand-name{font-family:"Plus Jakarta Sans",sans-serif;font-weight:700;color:var(--silver);letter-spacing:.06em;white-space:nowrap}
  .tagline{position:absolute;left:0;right:0;text-align:center;font-family:"Plus Jakarta Sans",sans-serif;font-weight:500;color:var(--white)}
  .card--front .brand-block{left:167px;top:108px;width:487px;height:191px;gap:18px;padding-top:10px}
  .card--front .brand-mark{width:90px;height:90px}
  .card--front .brand-name{font-size:30px}
  .card--front .tagline{top:326px;font-size:19px;line-height:31px}
  .back-panel{position:absolute;left:477px;top:-1px;width:345px;height:198px;background:var(--brand-blue)}
  .back-panel .brand-block{left:0;top:0;width:335px;height:138px;gap:12px;padding-top:8px}
  .back-panel .brand-mark{width:64px;height:64px}
  .back-panel .brand-name{font-size:20px}
  .back-panel .tagline{top:140px;font-size:13px;line-height:22px}
  .person{position:absolute;left:57px;top:135px}
  .person__name{font-family:"Fira Sans Condensed",sans-serif;font-weight:600;font-size:33px;color:var(--brand-blue);line-height:1}
  .person__role{font-family:"Fira Sans Condensed",sans-serif;font-weight:400;font-size:24px;color:var(--ink);margin-top:8px;line-height:1}
  .contact{position:absolute;left:-1px;height:40px;width:564px}
  .contact__tab{position:absolute;left:0;top:0;width:96px;height:100%;display:flex;align-items:center;justify-content:flex-end;padding-right:10px}
  .contact__tab svg{width:22px;height:22px}
  .contact__text{position:absolute;left:111px;top:6px;font-family:Lato,sans-serif;font-size:25px;color:var(--ink);line-height:1.1;white-space:nowrap}
  .contact__rule{position:absolute;left:96px;right:0;bottom:0;height:2px}
  .is-blue .contact__tab{background:var(--brand-blue)}
  .is-blue .contact__rule{background:var(--brand-blue)}
  .is-steel .contact__tab{background:var(--steel)}
  .is-steel .contact__rule{background:var(--steel)}
  .contact--address .contact__text{left:106px;line-height:32px;top:2px}
</style>
</head>
<body>
<div class="canvas">

  <section class="card card--front">
    <div class="brand-block">
      <div class="brand-mark"></div>
      <div class="brand-name">TRAVENIC EXTRUSION</div>
    </div>
    <p class="tagline">Diseño, extrusion, lacado, anodizado<br>y mecanizado de precisión de aluminio</p>
  </section>

  <section class="card card--back">
    <div class="back-panel">
      <div class="brand-block">
        <div class="brand-mark"></div>
        <div class="brand-name">TRAVENIC EXTRUSION</div>
      </div>
      <p class="tagline">Diseño, extrusion, lacado, anodizado<br>y mecanizado de precisión de aluminio</p>
    </div>

    <div class="person">
      <div class="person__name">MARCOS RUEDA LINARES</div>
      <div class="person__role">COMERCIAL</div>
    </div>

    <div class="contact is-blue" style="top:212px">
      <div class="contact__tab">
        <svg viewBox="0 0 24 24" fill="none" stroke="#fff" stroke-width="2"><rect x="6" y="2" width="12" height="20" rx="2.5"/><circle cx="12" cy="18" r="1" fill="#fff"/></svg>
      </div>
      <div class="contact__text">600 12 34 56</div>
      <div class="contact__rule"></div>
    </div>

    <div class="contact is-steel" style="top:252px">
      <div class="contact__tab">
        <svg viewBox="0 0 24 24" fill="none" stroke="#fff" stroke-width="1.8"><circle cx="12" cy="12" r="9"/><ellipse cx="12" cy="12" rx="4" ry="9"/><path d="M3 12h18M5 7h14M5 17h14"/></svg>
      </div>
      <div class="contact__text">www.travenic-ext.com</div>
      <div class="contact__rule"></div>
    </div>

    <div class="contact is-blue" style="top:292px">
      <div class="contact__tab">
        <svg viewBox="0 0 24 24" fill="none" stroke="#fff" stroke-width="1.8"><rect x="2" y="5" width="20" height="14" rx="1"/><path d="M2 5l10 8 10-8M2 19l7-7M22 19l-7-7"/></svg>
      </div>
      <div class="contact__text">marcosrueda@travenic-ext.com</div>
      <div class="contact__rule"></div>
    </div>

    <div class="contact contact--address is-steel" style="top:335px">
      <div class="contact__tab">
        <svg viewBox="0 0 24 24" fill="#fff"><path d="M12 2a7 7 0 0 0-7 7c0 5 7 13 7 13s7-8 7-13a7 7 0 0 0-7-7zm0 9.5A2.5 2.5 0 1 1 12 6.5a2.5 2.5 0 0 1 0 5z"/></svg>
      </div>
      <div class="contact__text">Pol. Ind. Los Olivos - C/4 No 22<br>41700 DOS HERMANAS (Sevilla)<br>Apartado de Correos 305</div>
    </div>
  </section>

</div>
</body>
</html>
```